Groovy little Insurance brokerage needs a new look

We have a new logo, but need to work out how to make it work for us!
We are a small insurance broking firm (three staff with different focus and styles), with lots of energy, experience and enthusiasm. A focus on both commercial and domestic market. We would like our cards to show a fresh look - while veering away from the 'run of the mill' insurance industry (often dull) approach.
Updates

Thanks to all for your concepts.

Had some great ideas come back, now just the process of picking which one is going to work best for us...
Will advise when we've had an opportunity to review.

Thanks!
From the team at
Kestrel Dunmore Insurance Brokers

Thanks SO much to all of your for your great designs.  Now just a process of sorting out the favorites.  If yours is eliminated, just want to say a collective thank you for your efforts!

Industry/Entity Type

Business

```html
<!DOCTYPE html>
<html lang="en">
<head>
<meta charset="utf-8">
<title>Kestrel Dunmore Insurance Brokers – Business Cards</title>
<link rel="stylesheet" href="https://fonts.googleapis.com/css2?family=Ubuntu:wght@400;500;700&display=swap">
<style>
  :root {
    --backdrop: #2a2a2a;
    --card: #ffffff;
    --ink: #1d1b1c;
    --ink-soft: #3a3a3a;
    --teal: #13afc4;
    --teal-deep: #0fa3b8;
    --sky: #aad8e3;
  }
  * { box-sizing: border-box; margin: 0; padding: 0; }
  html, body {
    width: 1200px; height: 1000px; overflow: hidden;
    background: var(--backdrop);
    font-family: "Ubuntu", sans-serif;
  }
  .stage {
    position: relative; width: 1200px; height: 1000px;
    display: flex; align-items: center; justify-content: center; gap: 40px;
  }
  .card {
    position: relative; width: 540px; height: 310px;
    background: var(--card); overflow: hidden;
  }
  .card__waves { position: absolute; inset: 0; width: 100%; height: 100%; }
  .card__web {
    position: absolute; left: 0; right: 0; bottom: 26px;
    text-align: center; color: #fff; font-size: 15px; letter-spacing: 2px;
  }

  /* Front */
  .brand {
    position: absolute; left: 40px; top: 70px;
    display: flex; align-items: center; gap: 16px;
  }
  .brand__square { width: 64px; height: 64px; background: var(--teal); flex: none; }
  .brand__name {
    color: var(--ink); font-weight: 700; font-size: 30px; line-height: 1.05;
    max-width: 360px;
  }

  /* Back */
  .person { position: absolute; left: 34px; top: 34px; color: var(--ink-soft); }
  .person__name { font-size: 21px; font-weight: 700; color: var(--ink); }
  .person__role { font-size: 12px; margin-bottom: 18px; }
  .person__line { font-size: 13px; line-height: 1.5; }
  .office { position: absolute; left: 290px; top: 84px; color: var(--ink-soft); font-size: 13px; line-height: 1.5; }
  .office__name { font-weight: 700; color: var(--ink); }
  .office__row { display: flex; align-items: center; gap: 7px; }
  .office__icon { width: 14px; height: 14px; flex: none; }
</style>
</head>
<body>
<main class="stage">
  <section class="card card--front">
    <svg class="card__waves" viewBox="0 0 540 310" preserveAspectRatio="none" aria-hidden="true">
      <path d="M0,185 C150,160 330,250 540,170 L540,310 L0,310Z" fill="var(--sky)"/>
      <path d="M0,232 C170,215 360,250 540,195 L540,310 L0,310Z" fill="var(--teal)"/>
      <path d="M0,275 C180,255 360,280 540,240 L540,310 L0,310Z" fill="var(--teal-deep)" opacity=".5"/>
    </svg>
    <div class="brand">
      <span class="brand__square"></span>
      <span class="brand__name">Kestrel Dunmore Insurance Brokers</span>
    </div>
    <p class="card__web">www.kdib.com</p>
  </section>

  <section class="card card--back">
    <svg class="card__waves" viewBox="0 0 540 310" preserveAspectRatio="none" aria-hidden="true">
      <path d="M0,195 C150,170 330,250 540,175 L540,310 L0,310Z" fill="var(--sky)"/>
      <path d="M0,238 C170,220 360,255 540,200 L540,310 L0,310Z" fill="var(--teal)"/>
      <path d="M0,278 C180,258 360,282 540,245 L540,310 L0,310Z" fill="var(--teal-deep)" opacity=".5"/>
    </svg>
    <div class="person">
      <h1 class="person__name">Martin Hollis</h1>
      <p class="person__role">accountant</p>
      <p class="person__line">+359 2 444 7120</p>
      <p class="person__line">martin@kdib.com</p>
    </div>
    <div class="office">
      <p class="office__name">Kestrel Dunmore Insurance Brokers</p>
      <p>18-20 Harbour Lane, 2210 Alder</p>
      <p class="office__row">
        <svg class="office__icon" viewBox="0 0 14 14" aria-hidden="true"><rect width="14" height="14" fill="var(--teal)"/><path d="M4,3 L6,3 L6.5,5.5 L5.5,6.3 Q6.5,8 8,8.7 L8.8,7.6 L11,8 L11,10 Q7,11 3.5,6 Q3,4 4,3Z" fill="#fff"/></svg>
        +88 (0) 7777 12345
      </p>
      <p class="office__row">
        <svg class="office__icon" viewBox="0 0 14 14" aria-hidden="true"><rect width="14" height="14" fill="var(--teal)"/><rect x="2.5" y="4" width="9" height="6.5" fill="none" stroke="#fff" stroke-width="1"/><path d="M2.5,4 L7,8 L11.5,4" fill="none" stroke="#fff" stroke-width="1"/></svg>
        info@kdib.com
      </p>
    </div>
    <p class="card__web">www.kdib.com</p>
  </section>
</main>
</body>
</html>
```